Anzeigengestaltung für Workshops
Zielgruppe
Die KTW-Academy realisiert Workshops für Medienschaffende. Im konkreten Fall soll ein 1-tägiger Workshop für Sprecher*innen in Radio, Podcast und Voice-Over beworben werden.
Aufgabenstellung
Die Anzeige soll in den verschiedenen Social-Media-Kanälen ausgespielt werden. Sie soll cool sein, eher minimalistisch, keinesfalls verspielt oder knallig.
Textbausteine sind:
Die Kunst des ruhigen Atems bei Tag [das ist der Titel der Veranstaltung]
Wie Du gut rüberkommst als Sprecher*in in Radio, Podcast und Voice-Over [das ist die Unterzeile]
Präsenz-Training | KTW-Funkhaus | 15.9.2023 [das sind die Rahmendaten]
ggfs. mit Störer 'jetzt buchen' o.ä.
Logo und Bild der Trainerin sind verpflichtend

```html
<!DOCTYPE html>
<html lang="de">
<head>
<meta charset="utf-8">
<title>KTW-Academy – Workshop-Anzeige</title>
<link rel="stylesheet" href="https://fonts.googleapis.com/css2?family=Poppins:wght@800&family=Source+Sans+3:wght@400;600;700&display=swap">
<style>
  :root {
    --green: #9ccb3b;
    --green-light: #b7d534;
    --white: #ffffff;
    --orange-start: #fdc617;
    --orange-end: #f6a124;
    --ink: #111111;
    --photo-top: #c9a88f;
    --photo-bottom: #2a302c;
  }
  * { margin: 0; padding: 0; box-sizing: border-box; }
  html, body { width: 1200px; height: 1200px; overflow: hidden; background: var(--white); }
  .ad {
    position: relative;
    width: 1200px;
    height: 1200px;
    background: var(--white);
    font-family: "Source Sans 3", sans-serif;
    color: var(--white);
    overflow: hidden;
  }
  .ad__stage {
    position: absolute;
    left: 0; top: 0;
    width: 1200px; height: 1091px;
    background: var(--green);
    overflow: hidden;
  }
  .ad__glow {
    position: absolute;
    left: 300px; top: -40px;
    width: 900px; height: 820px;
  }
  .brand {
    position: absolute;
    left: 70px; top: 62px;
    display: flex;
    align-items: center;
    gap: 14px;
    font-family: "Source Sans 3", sans-serif;
    font-weight: 700;
    font-size: 46px;
    color: var(--white);
    letter-spacing: 0.5px;
  }
  .brand__dot {
    width: 30px; height: 30px;
    background: var(--white);
  }
  .trainer-photo {
    position: absolute;
    left: 290px; top: 70px;
    width: 572px; height: 482px;
  }
  .headline {
    position: absolute;
    left: 0; top: 528px;
    width: 1200px;
    display: flex;
    flex-direction: column;
    align-items: center;
    font-family: "Poppins", sans-serif;
    font-weight: 800;
    text-transform: uppercase;
    font-size: 60px;
    line-height: 1;
    color: var(--white);
  }
  .headline__bar {
    display: inline-block;
    padding: 28px 46px 24px;
    background: linear-gradient(90deg, var(--orange-start), var(--orange-end));
    transform: rotate(-1.3deg);
    box-shadow: 0 6px 14px rgba(0,0,0,0.12);
    white-space: nowrap;
  }
  .headline__bar--second { margin-top: -14px; }
  .subline {
    position: absolute;
    left: 0; top: 770px;
    width: 1200px;
    text-align: center;
    font-weight: 600;
    font-size: 38px;
    line-height: 1.45;
    transform: rotate(-2deg);
  }
  .facts {
    position: absolute;
    left: 0; top: 928px;
    width: 1200px;
    text-align: center;
    font-weight: 600;
    font-size: 44px;
    white-space: nowrap;
  }
  .cta {
    position: absolute;
    left: 366px; top: 1041px;
    width: 470px; height: 101px;
    border-radius: 22px;
    background: linear-gradient(180deg, var(--orange-start), var(--orange-end));
    box-shadow: 0 10px 22px rgba(0,0,0,0.18);
    display: flex;
    align-items: center;
    justify-content: center;
    font-weight: 700;
    font-size: 50px;
    color: var(--white);
    letter-spacing: 0.5px;
  }
</style>
</head>
<body>
  <main class="ad">
    <section class="ad__stage">
      <svg class="ad__glow" viewBox="0 0 900 820" aria-hidden="true">
        <defs>
          <radialGradient id="stageGlow" cx="0.6" cy="0.4" r="0.55">
            <stop offset="0" stop-color="var(--green-light)" stop-opacity="0.8"/>
            <stop offset="1" stop-color="var(--green-light)" stop-opacity="0"/>
          </radialGradient>
        </defs>
        <rect width="900" height="820" fill="url(#stageGlow)"/>
      </svg>

      <div class="brand">
        <span class="brand__dot"></span>
        <span class="brand__name">KTW-Academy</span>
      </div>

      <svg class="trainer-photo" viewBox="0 0 572 482" role="img" aria-label="Porträtfoto der Trainerin, lächelnd, in dunklem Oberteil">
        <defs>
          <linearGradient id="photoTone" x1="0" y1="0" x2="0" y2="1">
            <stop offset="0" stop-color="var(--photo-top)"/>
            <stop offset="0.7" stop-color="#b8927c"/>
            <stop offset="1" stop-color="var(--photo-bottom)"/>
          </linearGradient>
        </defs>
        <path d="M0 482 C20 400 120 370 190 340 L190 60 Q286 0 382 60 L382 340 C452 370 552 400 572 482 Z" fill="url(#photoTone)"/>
      </svg>
    </section>

    <h1 class="headline">
      <span class="headline__bar">Die Kunst des ruhigen</span>
      <span class="headline__bar headline__bar--second">Atems bei Tag</span>
    </h1>

    <p class="subline">Wie Du gut rüberkommst als Sprecher*in<br>in Radio, Podcast und Voice-Over</p>

    <p class="facts">Präsenz-Training | KTW-Funkhaus | 15.9.2023</p>

    <div class="cta">JETZT BUCHEN</div>
  </main>
</body>
</html>
```